Plakate für eine Veranstaltung
Sehr professionelle Umsetzung, schnelle Absprachen und freundlicher Kontakt. Immer wieder gerne, vielen Dank lieber Karvano.
Zielgruppe
Musikerin / Sängerin, Wir suchen ein hochwertiges Plakat mit unseren Specials Guests für ein Publikum mittleren Alters.
Aufgabenstellung
Anlage in Din1, Titel der Veranstaltung: 'Velvet Lantern Serenade' - Petra Holwig & Friends in concert, hochauflösende Bilder sind fast komplett vorhanden, gerne erst mal mit vorhandenen Material Idee kreieren und im Anschluss austauschen. Details zum Konzert: 16.11.23, Bühnenhaus am Ulmenfeld Lingen, 19.30 Uhr, Veranstalter: Stadt Lingen. Gerne die Hauptsängerin im Fokus und die anderen Aktiven in Einblendung einarbeiten. Name der Special Guest stehen als Dateiname in den angehängten Files.

```html
<!DOCTYPE html>
<html lang="de">
<head>
<meta charset="utf-8">
<title>Petra Holwig &amp; Friends in Concert – Velvet Lantern Serenade</title>
<link rel="stylesheet" href="https://fonts.googleapis.com/css2?family=Archivo:wght@800&family=Dancing+Script:wght@700&family=Bangers&family=Figtree:wght@300;400;600&display=swap">
<style>
  :root {
    --page-bg: #ffffff;
    --night: #232222;
    --brown-deep: #1e1410;
    --gold: #e8c24e;
    --white: #ffffff;
  }
  html, body {
    margin: 0;
    width: 1000px;
    height: 1200px;
    overflow: hidden;
    background: var(--page-bg);
  }
  .poster-frame {
    position: absolute;
    left: 75.5px;
    top: 0;
    width: 1078px;
    height: 1524px;
    transform: scale(0.7874);
    transform-origin: 0 0;
    overflow: hidden;
    background: var(--brown-deep);
  }
  .poster-art {
    position: absolute;
    inset: 0;
    width: 1078px;
    height: 1524px;
  }
  .headline {
    position: absolute;
    right: 44px;
    top: 178px;
    margin: 0;
    text-align: right;
    color: var(--white);
  }
  .headline-name {
    display: block;
    font-family: "Archivo", sans-serif;
    font-weight: 800;
    font-size: 98px;
    line-height: 1;
    letter-spacing: -1px;
  }
  .headline-friends,
  .headline-concert {
    display: block;
    font-family: "Dancing Script", cursive;
    font-weight: 700;
    line-height: 1;
  }
  .headline-friends { font-size: 100px; margin: 12px 48px 0 0; }
  .headline-concert { font-size: 94px; margin-top: -4px; }
  .event-title {
    font-family: "Bangers", cursive;
    font-size: 88px;
    fill: var(--gold);
    letter-spacing: 2px;
  }
  .guest-label {
    position: absolute;
    top: 1184px;
    height: 49px;
    background: var(--night);
    color: var(--white);
    font-family: "Figtree", sans-serif;
    font-weight: 400;
    font-size: 20px;
    letter-spacing: -0.3px;
    display: flex;
    align-items: center;
    justify-content: center;
  }
  .guest-label--violin { left: 50px; width: 286px; }
  .guest-label--piano { left: 395px; width: 287px; }
  .guest-label--pipes { left: 733px; width: 304px; }
  .event-details {
    position: absolute;
    left: 56px;
    top: 1330px;
    color: var(--white);
    font-family: "Figtree", sans-serif;
  }
  .event-date {
    margin: 0;
    font-weight: 600;
    font-size: 64px;
    line-height: 1;
  }
  .event-venue {
    margin: 8px 0 0;
    font-weight: 300;
    font-size: 52px;
    line-height: 1.1;
  }
</style>
</head>
<body>
  <main class="poster-frame">
    <svg class="poster-art" viewBox="0 0 1078 1524" xmlns="http://www.w3.org/2000/svg">
      <defs>
        <linearGradient id="bgTop" x1="0" y1="0" x2="1" y2="1">
          <stop offset="0" stop-color="#241812"/>
          <stop offset="1" stop-color="#4a3626"/>
        </linearGradient>
        <linearGradient id="choirTone" x1="0" y1="0" x2="1" y2="0">
          <stop offset="0" stop-color="#4a3828" stop-opacity="0"/>
          <stop offset="0.35" stop-color="#4d3b2b"/>
          <stop offset="1" stop-color="#5e4a38"/>
        </linearGradient>
        <linearGradient id="goldWave" x1="0" y1="0" x2="1" y2="0">
          <stop offset="0" stop-color="#9a7a44"/>
          <stop offset="0.55" stop-color="#e9dc9c"/>
          <stop offset="1" stop-color="#b8944f"/>
        </linearGradient>
        <linearGradient id="goldField" x1="0" y1="0" x2="1" y2="1">
          <stop offset="0" stop-color="#8c6c42"/>
          <stop offset="0.5" stop-color="#c4a06a"/>
          <stop offset="1" stop-color="#a88550"/>
        </linearGradient>
        <linearGradient id="singerTone" x1="0" y1="0" x2="1" y2="1">
          <stop offset="0" stop-color="#1a0e0c"/>
          <stop offset="0.45" stop-color="#5a2a22"/>
          <stop offset="1" stop-color="#7a4a3a"/>
        </linearGradient>
        <linearGradient id="violinTone" x1="0" y1="0" x2="1" y2="1">
          <stop offset="0" stop-color="#2a0c12"/>
          <stop offset="1" stop-color="#7a1e36"/>
        </linearGradient>
        <linearGradient id="pianoTone" x1="0" y1="0" x2="0" y2="1">
          <stop offset="0" stop-color="#f2f2f2"/>
          <stop offset="1" stop-color="#d9d2cb"/>
        </linearGradient>
        <linearGradient id="pipesTone" x1="0" y1="0" x2="1" y2="1">
          <stop offset="0" stop-color="#2c4a30"/>
          <stop offset="1" stop-color="#33507a"/>
        </linearGradient>
        <linearGradient id="cameraTone" x1="0" y1="0" x2="0" y2="1">
          <stop offset="0" stop-color="#e3b94d" stop-opacity="0.55"/>
          <stop offset="1" stop-color="#e3b94d" stop-opacity="0.15"/>
        </linearGradient>
        <clipPath id="singerClip">
          <path d="M0 150 C 60 90 150 60 260 55 C 450 50 590 200 590 380 C 590 470 570 540 560 560 L 0 700 Z"/>
        </clipPath>
      </defs>

      <rect class="backdrop" width="1078" height="1524" fill="url(#bgTop)"/>
      <rect class="choir-photo" x="480" y="0" width="598" height="560" fill="url(#choirTone)" role="img" aria-label="Foto: Chor auf der Bühne, sepiafarben"/>
      <rect class="reel-ornament" x="900" y="0" width="178" height="170" fill="#c9a24a" opacity="0.12" role="img" aria-label="Dekor: Filmrolle und Schneeflocken"/>

      <rect class="singer-photo" x="0" y="50" width="600" height="660" fill="url(#singerTone)" clip-path="url(#singerClip)" role="img" aria-label="Foto: Hauptsängerin mit Mikrofon auf der Bühne"/>

      <g class="sparkles" fill="var(--white)">
        <path d="M262 33 L268 57 L292 63 L268 69 L262 93 L256 69 L232 63 L256 57 Z"/>
        <path d="M369 65 L373 79 L387 83 L373 87 L369 101 L365 87 L351 83 L365 79 Z"/>
        <path d="M576 463 L584 490 L611 498 L584 506 L576 533 L568 506 L541 498 L568 490 Z"/>
        <path d="M614 463 L616 471 L624 473 L616 475 L614 483 L612 475 L604 473 L612 471 Z"/>
      </g>

      <path class="gold-wave" d="M0 682 C 250 690 450 520 700 500 C 850 488 960 500 1078 515 L1078 1524 L0 1524 Z" fill="url(#goldWave)"/>
      <rect class="gold-field" x="0" y="780" width="1078" height="560" fill="url(#goldField)"/>
      <rect class="snowflake-ornament" x="985" y="525" width="93" height="160" fill="#7a6a52" opacity="0.3" role="img" aria-label="Dekor: Schneeflocke"/>

      <path class="title-band" d="M0 700 C 300 700 500 560 780 563 C 900 565 1000 575 1078 585 L1078 830 C 950 800 850 780 700 800 C 500 830 350 890 230 885 C 120 880 60 855 0 848 Z" fill="var(--night)"/>
      <path id="titleCurve" d="M122 840 C 330 840 520 760 700 710 C 820 680 920 690 1000 740" fill="none"/>
      <text class="event-title"><textPath href="#titleCurve" textLength="900" lengthAdjust="spacingAndGlyphs">VELVET LANTERN SERENADE</textPath></text>

      <circle class="guest-photo" cx="193" cy="1026" r="137" fill="url(#violinTone)" role="img" aria-label="Foto: Violinistin mit Lichteffekten"/>
      <circle class="guest-photo" cx="539" cy="1026" r="137" fill="url(#pianoTone)" role="img" aria-label="Foto: Porträt des Pianisten"/>
      <circle class="guest-photo" cx="885" cy="1026" r="137" fill="url(#pipesTone)" role="img" aria-label="Foto: Dudelsackspieler in Uniform"/>

      <path class="footer-band" d="M0 1280 C 200 1262 400 1268 600 1298 C 800 1330 950 1322 1078 1302 L1078 1524 L0 1524 Z" fill="var(--night)"/>
      <path class="camera-ornament" d="M955 1360 L1078 1300 L1078 1524 L955 1524 Z" fill="url(#cameraTone)" role="img" aria-label="Dekor: Filmkamera auf Stativ"/>
    </svg>

    <h1 class="headline">
      <span class="headline-name">PETRA HOLWIG</span>
      <span class="headline-friends">&amp; Friends</span>
      <span class="headline-concert">in Concert</span>
    </h1>

    <div class="guest-label guest-label--violin">Lena Marquardt I Violistin</div>
    <div class="guest-label guest-label--piano">Tobias Reinholt I Pianist</div>
    <div class="guest-label guest-label--pipes">Heideland Pipes &amp; Drums</div>

    <div class="event-details">
      <p class="event-date">16.11. 2023, 19.30 Uhr</p>
      <p class="event-venue">Bühnenhaus am Ulmenfeld in Lingen</p>
    </div>
  </main>
</body>
</html>
```